Business Card Design

A new interior design company specialising in residential property styling, with a focus on styling properties for sale. We aim to present the property to increase marketability, saleability and hopefully get the best price.
We are looking for a design that stands out from the crowd maybe using colour and maybe pattern, something that is modern and fits in with companies aesthetic of design.
We would like the design not to be too fussy, with perhaps all of the contact information on the back (ie just the company name on front?)

Industry/Entity Type

Residential

Contact Information for Business Card

Brisa Interiors, Tessa Wingrove, Interior Designer,0417365209, brisainteriors@quolmail.com.au

Requirements
Nice to have
• Brisa means "love" in Spanish and I was wondering whether it might be too corny to use the M in bRisa that resembles a love heart, something curvy. This is just an idea I've was toying with and I am completely open to other suggestions.

```html
<!DOCTYPE html>
<html lang="en">
<head>
<meta charset="utf-8">
<title>Brisa Interiors — Business Card</title>
<link rel="stylesheet" href="https://fonts.googleapis.com/css2?family=Lato:wght@300;400&display=swap">
<style>
  :root {
    --backdrop: #2a2a2c;
    --front-blue: #6b85a6;
    --back-blush: #e7b8ac;
    --ink-plum: #6a5a72;
    --ink-white: #ffffff;
  }
  * { margin: 0; padding: 0; box-sizing: border-box; }
  html, body { width: 1200px; height: 1000px; overflow: hidden; }
  body {
    background: var(--backdrop);
    font-family: "Lato", sans-serif;
    position: relative;
  }
  .card {
    position: absolute;
    width: 500px;
    height: 290px;
    border-radius: 12px;
    box-shadow: 0 10px 30px rgba(0,0,0,0.45);
  }
  .card-front {
    left: 70px; top: 500px;
    background: var(--front-blue);
    display: flex; align-items: center; justify-content: center;
  }
  .brand-name {
    color: var(--ink-white);
    font-weight: 400;
    font-size: 42px;
    letter-spacing: 0.5px;
  }
  .card-back {
    left: 630px; top: 210px;
    background: var(--back-blush);
    color: var(--ink-plum);
  }
  .person-name {
    position: absolute; left: 28px; top: 22px;
    font-size: 20px; font-weight: 400;
  }
  .person-title {
    position: absolute; left: 28px; top: 46px;
    font-size: 17px; font-weight: 300;
  }
  .dimension-line { position: absolute; left: 0; top: 0; }
  .contact-list {
    position: absolute; left: 250px; top: 214px;
    list-style: none; font-size: 15px; font-weight: 300;
  }
  .contact-list li { display: flex; align-items: center; gap: 8px; height: 24px; }
  .contact-list svg { flex: none; }
</style>
</head>
<body>
  <section class="card card-front" aria-label="Card front">
    <span class="brand-name">Brisa Interiors</span>
  </section>

  <section class="card card-back" aria-label="Card back">
    <div class="person-name">Tessa Wingrove</div>
    <div class="person-title">Interior Designer</div>

    <svg class="dimension-line" width="500" height="290" viewBox="0 0 500 290" aria-hidden="true">
      <g stroke="#6a5a72" stroke-width="1.2" fill="#6a5a72">
        <line x1="160" y1="68" x2="330" y2="68"/>
        <line x1="240" y1="200" x2="310" y2="200"/>
        <line x1="290" y1="72" x2="290" y2="196"/>
        <path d="M290 68 l-4 10 h8 z" stroke="none"/>
        <path d="M290 200 l-4 -10 h8 z" stroke="none"/>
      </g>
    </svg>

    <ul class="contact-list">
      <li>
        <svg width="12" height="14" viewBox="0 0 12 14" aria-hidden="true">
          <rect x="2" y="0.5" width="8" height="13" rx="1.5" fill="#6a5a72"/>
          <rect x="3.5" y="2" width="5" height="7" fill="#e7b8ac"/>
        </svg>
        <span>0417 365 209</span>
      </li>
      <li>
        <svg width="14" height="11" viewBox="0 0 14 11" aria-hidden="true">
          <rect x="0.5" y="0.5" width="13" height="10" fill="#6a5a72"/>
          <path d="M0.5 0.5 L7 6 L13.5 0.5" fill="none" stroke="#e7b8ac" stroke-width="1.2"/>
        </svg>
        <span>brisainteriors@quolmail.com.au</span>
      </li>
    </ul>
  </section>
</body>
</html>
```